Business Cards Design for the electrical wholesaler: clean bold dynamic :)

We need a business card design that would follow our latest brand guidelines. As an electrical wholesaler we want to bring a fresh look and feel into the industry. The design should be clean bold and dynamic. It should come alive with the renewed energy of our green colour. Our grey colour should keep things balanced and complement the notion of maturity and responsibility. We employ Lato as a corporate font however are not bound by this font and we’re open to interpretation here.

Target Market(s)

Electrical contractors

Industry/Entity Type

Business

Contact Information for Business Card

Logo
Name & Surname: Olena Dovbush
Job Title: Director of Marketing
Email: helen.dovbush@mailvane.example
Cell phone: XXX.XXX.XXXX
Address: 20917 - 87 Ave. Edmonton, AB, Canada. T6K 2R8
Business Phone: 780.555.0187
Website: www.qorvil.example

Font styles to use
Other font styles liked:
• Lato

Requirements
Must have
• Logo & website
Nice to have
• Brand elements - some of them you may find in the attached Brand Guidelines (e.g. three lines on the background signifying "W")

```html
<!DOCTYPE html>
<html lang="en">
<head>
<meta charset="utf-8">
<title>Qorvil business card</title>
<link rel="stylesheet" href="https://fonts.googleapis.com/css2?family=Lato:wght@400;700&display=swap">
<style>
  :root {
    --backdrop: #2b2b2b;
    --paper: #f2f2f2;
    --grey: #4d4e50;
    --grey-text: #4a4a4c;
    --green: #8cc63f;
    --green-back: #86c13c;
    --white: #ffffff;
  }
  * { margin: 0; padding: 0; box-sizing: border-box; }
  html, body {
    width: 1200px; height: 960px; overflow: hidden;
    background: var(--backdrop);
    font-family: "Lato", Arial, sans-serif;
  }
  .canvas { position: relative; width: 1200px; height: 960px; }
  .card {
    position: absolute; width: 600px; height: 342px;
    border-radius: 22px; overflow: hidden;
  }
  .card-front { left: 314px; top: 113px; background: var(--paper); }
  .card-back { left: 311px; top: 472px; background: var(--green-back); }

  .brand { position: absolute; display: flex; align-items: center; gap: 10px; }
  .brand-mark { width: 30px; height: 30px; border-radius: 4px; }
  .brand-name { font-weight: 700; line-height: 1; }
  .card-front .brand { left: 38px; top: 48px; }
  .card-front .brand-mark { background: var(--green); }
  .card-front .brand-name { color: var(--grey); font-size: 44px; }
  .card-back .brand { left: 50%; top: 135px; transform: translateX(-50%); gap: 14px; }
  .card-back .brand-mark { width: 40px; height: 40px; background: var(--white); }
  .card-back .brand-name { color: var(--white); font-size: 60px; }

  .person {
    position: absolute; left: 329px; top: 57px; width: 280px;
    text-align: center; white-space: nowrap;
  }
  .person-name { color: var(--green); font-weight: 700; font-size: 23px; line-height: 1.1; }
  .person-title { color: var(--grey-text); font-size: 15px; letter-spacing: 0.3px; }

  .band { position: absolute; left: 0; top: 148px; width: 600px; height: 146px; display: flex; }
  .band-grey { width: 400px; background: var(--grey); }
  .band-green { flex: 1; background: var(--green); }

  .contacts { position: absolute; left: 38px; top: 174px; list-style: none; }
  .contacts li {
    display: flex; align-items: center; gap: 8px;
    color: var(--white); font-size: 14.5px; line-height: 19px;
  }
  .contacts svg, .address svg { width: 15px; height: 15px; fill: var(--green); flex: none; }

  .address {
    position: absolute; left: 40px; top: 306px;
    display: flex; align-items: center; gap: 6px;
    color: var(--grey-text); font-size: 14.5px;
  }

  .site {
    position: absolute; left: 0; right: 0; top: 292px; text-align: center;
    color: var(--white); font-size: 13px; letter-spacing: 3.4px;
  }
</style>
</head>
<body>
<main class="canvas">
  <section class="card card-front" aria-label="Card front">
    <div class="brand">
      <span class="brand-mark"></span>
      <span class="brand-name">qorvil</span>
    </div>
    <div class="person">
      <p class="person-name">DANA VERLOW</p>
      <p class="person-title">CEO/FOUNDER</p>
    </div>
    <div class="band"><div class="band-grey"></div><div class="band-green"></div></div>
    <ul class="contacts">
      <li><svg viewBox="0 0 16 16"><path d="M3 1l3 3-1.5 2a9 9 0 005.5 5.5L12 10l3 3-2 2C7 15 1 9 1 3z"/></svg>555 010 2538</li>
      <li><svg viewBox="0 0 16 16"><path d="M4 0h8a1 1 0 011 1v14a1 1 0 01-1 1H4a1 1 0 01-1-1V1a1 1 0 011-1zm1 2v10h6V2z"/></svg>555 010 9364</li>
      <li><svg viewBox="0 0 16 16"><path d="M4 1h8v4H4zM1 6h14v7h-3v2H4v-2H1zm4 5v3h6v-3z"/></svg>555 010 1940</li>
      <li><svg viewBox="0 0 16 16"><path d="M1 3h14v10H1zm1 1.5v.5l6 4 6-4v-.5z"/></svg>hello@qorvil.example</li>
      <li><svg viewBox="0 0 16 16"><circle cx="8" cy="8" r="7"/></svg>www.qorvil.example</li>
    </ul>
    <p class="address"><svg viewBox="0 0 16 16"><path d="M8 0a5.5 5.5 0 015.5 5.5C13.5 10 8 16 8 16S2.5 10 2.5 5.5A5.5 5.5 0 018 0zm0 3a2.5 2.5 0 100 5 2.5 2.5 0 000-5z"/></svg>1200 Fernleaf Way, Northvale, Example 00000</p>
  </section>

  <section class="card card-back" aria-label="Card back">
    <div class="brand">
      <span class="brand-mark"></span>
      <span class="brand-name">qorvil</span>
    </div>
    <p class="site">www.qorvil.example</p>
  </section>
</main>
</body>
</html>
```